Ledgerwise Reach - B2B Demand Generation Website Project

We need a fully functional website for www.ledgerwisereach.example. We are a B2B Demand Generation company, based in London, working with companies such as QRT, VKD, Norvex, Brindlow, Tarvo generating them sales leads for their sales teams. We run this through digital marketing newsletter promotions and have a network of websites. Content syndication, data, demand generation, online marketing. Our logo has just been redone (attached) and we have a holding page already which i would like to use the style / colours. Our logo is bright and vibrant but i dont want the site to be a rainbow. We are expensive, classy, professorial, B2B, intelligent.

Home
About Us
Our Services
Prospora & QA Technology
Intent Data
Testimonials
Contact Us
Updates

Target Market(s)

B2B Marketers (QRT, Velquarion, Tarvo, VKD, Opal Reach, Driftmoor, Harlow Quantis, Technology Companies, Data Companies, Marketing Teams, Tumbleden.

Industry/Entity Type

Marketing

Coding

Coded - Design and coding required

Number of Pages Required

5+ page

Font styles to use
Sans Serif

Requirements
Must have
• Home
About Us
Our Services
Prospora & QA Technology
Intent Data
Testimonials
Contact Us

Simple Pages.

Look classy, intelligent, data experts. I like the video homepages were the image moves at the top. Very soft animation.
Nice to have
• Websites i like:

https://www.vkd.example/
https://www.brevantor.example/
https://www.plumfieldsites.example.co.uk/

Ledgerwise Reach - The Demand Generation Company
Should not have
• Glimpsevault crap images

```html
<!DOCTYPE html>
<html lang="en">
<head>
<meta charset="utf-8">
<title>Ledgerwise Reach - The Demand Generation Company</title>
<link rel="stylesheet" href="https://fonts.googleapis.com/css2?family=Montserrat:ital,wght@0,300;0,400;0,500;0,600;0,700;1,300;1,400&display=swap">
<style>
:root{
  --ink:#1b1b28;
  --night:#141424;
  --navy:#0f1c3d;
  --navy-deep:#0a1530;
  --navy-mid:#1a2a52;
  --calc:#0b1414;
  --royal:#1d3466;
  --white:#ffffff;
  --muted:#c8cbd6;
  --grey:#8d93a6;
  --text:#22263a;
}
*{margin:0;padding:0;box-sizing:border-box}
html,body{width:1200px;height:5272px;overflow:hidden}
body{position:relative;background:var(--white);font-family:'Montserrat',sans-serif;color:var(--text)}
.abs{position:absolute}

/* header */
.site-header{left:0;top:0;width:1200px;height:102px;background:#2a2c3c;display:flex;align-items:center}
.brand{left:100px;top:34px;display:flex;align-items:center;gap:12px;color:var(--white)}
.brand-dot{width:40px;height:40px;border-radius:50%;border:2px solid var(--white)}
.brand-name{font-size:24px;font-weight:400;line-height:1}
.brand-tag{font-size:8px;letter-spacing:.5px;color:var(--muted);margin-top:3px}
.main-nav{left:372px;top:58px;display:flex;gap:40px;font-size:12px;color:var(--white);letter-spacing:.6px}
.btn-outline{border:2px solid var(--white);border-radius:6px;color:var(--white);font-weight:700;font-size:12px;display:flex;align-items:center;justify-content:center;letter-spacing:.5px}
.header-contact{left:1013px;top:45px;width:113px;height:44px}

/* hero */
.hero{left:0;top:102px;width:1200px;height:588px;background:linear-gradient(120deg,#2c3047 0%,#1d2035 55%,#292d43 100%)}
.hero-photo{left:720px;top:102px;width:480px;height:588px;background:linear-gradient(200deg,#f2f3f6 0%,#9aa0b0 45%,#3a3f55 100%)}
.hero-title{left:100px;top:264px;font-size:38px;font-weight:500;letter-spacing:5px;line-height:48px;color:var(--white)}
.hero-copy{left:100px;top:435px;width:460px;font-size:14px;line-height:15.5px;color:var(--white);letter-spacing:.4px}

/* about */
.process-panel{left:16px;top:1075px;width:1108px;height:774px;background:var(--ink)}
.process-strip{left:821px;top:1849px;width:303px;height:1000px;background:var(--ink)}
.process-edge{left:16px;top:1846px;width:805px;height:3px;background:var(--royal)}
.video{left:12px;top:708px;width:813px;height:510px;background:linear-gradient(135deg,#4b5178 0%,#6f7296 50%,#3d4166 100%)}
.play{left:363px;top:901px;width:122px;height:122px;border-radius:50%;background:var(--white)}
.about-title{left:850px;top:790px;font-size:28px;letter-spacing:3px;color:var(--text)}
.about-copy{left:850px;top:840px;width:270px;font-size:10px;line-height:10.5px;color:var(--text)}

.process-title{left:186px;top:1444px;font-size:28px;font-weight:500;letter-spacing:4px;line-height:35px;color:var(--white)}
.process-list{left:528px;top:1386px;width:430px;font-size:12.5px;line-height:13px;color:var(--white);list-style:none}
.process-list li{position:relative;margin-bottom:28px;padding-left:28px}
.process-list li::before{content:"";position:absolute;left:0;top:3px;width:7px;height:7px;border-radius:50%;background:var(--white)}
.process-list .sub{display:block;padding-left:18px}

.estimate{left:205px;top:1984px;font-size:30px;font-style:italic;font-weight:400;letter-spacing:3px;line-height:35px;color:var(--text)}

/* calculator */
.calculator{left:100px;top:2171px;width:1100px;height:495px;background:linear-gradient(110deg,#060d0c 0%,#101a1a 60%,#1b2428 100%)}
.calc-title{left:199px;top:2326px;font-size:24px;font-weight:500;letter-spacing:3px;color:var(--white)}
.calc-label{left:203px;top:2375px;font-size:12.5px;color:var(--white);letter-spacing:.5px}
.calc-input{left:203px;top:2408px;width:428px;height:35px;background:var(--white);border:none}
.calc-button{left:207px;top:2488px;width:229px;height:51px;border-radius:26px;background:var(--royal);color:var(--white);font-size:18px;letter-spacing:2px;display:flex;align-items:center;justify-content:center}

/* services */
.services-bg{left:16px;top:2765px;width:1108px;height:1581px;background:linear-gradient(180deg,#141c35 0%,var(--navy-mid) 20%,#15234a 45%,var(--navy) 100%)}
.services-box{left:47px;top:2894px;width:1053px;height:659px;border:2px solid #2a3a66;background:#16254a}
.services-feature{left:49px;top:2896px;width:1049px;height:397px;background:linear-gradient(100deg,#1c2b54,#213260)}
.services-title{left:156px;top:3030px;font-size:38px;font-weight:500;letter-spacing:4px;line-height:48px;color:var(--white)}
.feature-icon{left:545px;top:2942px}
.feature-title{left:539px;top:3033px;font-size:19px;font-weight:600;letter-spacing:1.5px;color:var(--white)}
.feature-copy{left:541px;top:3078px;width:450px;font-size:11.5px;line-height:13.5px;color:var(--white)}
.dots{display:flex;gap:4px}
.dots span{width:11px;height:11px;border-radius:50%;border:1.5px solid var(--white)}
.dots span.on{background:var(--white)}
.feature-dots{left:935px;top:3264px}
.service-col{top:3320px;width:370px;text-align:center;color:var(--white)}
.service-col h4{font-size:11.5px;font-weight:700;letter-spacing:.6px;margin-top:22px}
.service-col p{font-size:10.5px;line-height:11.5px;margin:16px auto 0;width:220px}
.service-divider{top:3350px;width:1px;height:160px;background:#3c4b77}

/* testimonials */
.voices{left:119px;top:3621px;width:1005px;height:254px;background:var(--white)}
.voices-text{left:0;top:3729px;width:1200px;text-align:center;padding-left:0;font-size:30px;font-style:italic;letter-spacing:3px;color:var(--text)}
.testimonials-title{left:156px;top:4094px;font-size:38px;font-weight:500;letter-spacing:4px;color:var(--white)}
.quote-card{left:702px;top:3922px;width:279px;height:338px;border-radius:18px;background:var(--white)}
.quote-mark{left:650px;top:3890px;font-size:320px;line-height:1;font-weight:700;color:#5c6274;font-family:'Montserrat',sans-serif}
.quote-label{left:718px;top:4065px;font-size:27px;font-weight:300;letter-spacing:3px;color:var(--text)}
.quote-copy{left:724px;top:4113px;width:245px;font-size:10.5px;font-style:italic;line-height:12px;color:var(--text)}
.quote-name{left:726px;top:4192px;font-size:13px;font-style:italic;letter-spacing:1px;color:var(--text)}
.quote-close{left:906px;top:4181px;width:76px;height:76px;border-radius:50%;background:var(--navy);color:var(--white);font-size:90px;font-weight:700;line-height:110px;text-align:center}
.quote-dots{left:935px;top:4272px}

/* apart */
.apart-side{left:0;top:4346px;width:113px;height:497px;background:var(--white)}
.apart-title{left:246px;top:4480px;font-size:34px;font-weight:500;letter-spacing:5px;color:var(--text)}
.apart-box{left:170px;top:4536px;width:997px;height:313px;background:var(--navy)}
.apart-sub{left:250px;top:4584px;font-size:19px;font-weight:500;letter-spacing:1.5px;color:var(--white)}
.apart-copy{left:252px;top:4638px;width:770px;font-size:11.5px;line-height:12.5px;color:var(--white)}
.wordmark{font-size:30px;font-weight:700;letter-spacing:2px;margin-right:6px;vertical-align:-3px}
.apart-copy p+p{margin-top:22px}

/* footer */
.site-footer{left:0;top:4843px;width:1200px;height:429px;background:linear-gradient(180deg,#05070f 0%,#0c1228 100%)}
.footer-side{left:0;top:4843px;width:113px;height:6px;background:#05070f}
.footer-brand{left:68px;top:4995px;text-align:center;color:var(--white)}
.footer-brand .brand-dot{margin:0 auto 14px;width:50px;height:50px}
.footer-brand .brand-name{font-size:24px}
.footer-rule{width:1px;height:237px;top:4965px;background:#525a72}
.footer-head{font-size:11.5px;font-weight:700;letter-spacing:.5px;color:var(--white)}
.footer-links{left:328px;top:4980px;list-style:none;font-size:12px;color:var(--white);letter-spacing:.5px}
.footer-links li{margin-top:21px}
.footer-tech{left:540px;top:4982px;width:166px;text-align:center;color:var(--white);font-size:12px}
.footer-tech .item{margin-top:22px}
.footer-location{left:560px;top:5140px;color:var(--white);font-size:12px}
.footer-about{left:772px;top:4980px;width:350px;color:var(--white)}
.footer-about p{font-size:10px;line-height:10.5px;margin-top:24px}
.footer-contact{left:972px;top:5126px;width:148px;height:52px;font-size:15px}
</style>
</head>
<body>

<header class="site-header abs">
  <div class="brand abs">
    <span class="brand-dot"></span>
    <div><div class="brand-name">ledgerwise reach</div><div class="brand-tag">The Demand Generation Company</div></div>
  </div>
  <nav class="main-nav abs"><span>About Us</span><span>Services</span><span>Testimonials</span><span>Intent Data</span><span>Prospora &amp; QA Technology</span></nav>
  <div class="btn-outline header-contact abs">Contact Us</div>
</header>

<section class="hero abs"></section>
<div class="hero-photo abs" role="img" aria-label="Photograph of a modern office tower with white striped balconies"></div>
<h1 class="hero-title abs">TOP DEMAND<br>GENERATION AGENCY<br>AT YOUR SERVICE</h1>
<p class="hero-copy abs">Ledgerwise Reach offers multi-channel demand generation services to publishers and technology vendors through our network of lead generation websites and native speaking telemarketing agents. Whether looking for MQL, ABM or BANT campaigns, Ledgerwise Reach can assist you in delivering your demand generation strategy and generate pipeline for your sales teams and/or channel partners.</p>

<div class="process-panel abs"></div>
<div class="process-strip abs"></div>
<div class="process-edge abs"></div>
<div class="video abs" role="img" aria-label="Video still of a team working at laptops around a meeting table"></div>
<svg class="play abs" viewBox="0 0 122 122" aria-label="Play video"><circle cx="61" cy="61" r="61" fill="#fff"/><path d="M48 40 L84 61 L48 82 Z" fill="#2b2f45"/></svg>
<h2 class="about-title abs">About Us</h2>
<p class="about-copy abs">Ledgerwise Reach can deliver high quality sales leads from any country in the world. This can include leads via email or telemarketing, account-based targeting (ABM) or identifying need and pain points through BANT / SQL campaigns.</p>

<h2 class="process-title abs">HOW DOES<br>THE PROCESS<br>OF DEMAND<br>GENERATION<br>WORK?</h2>
<ul class="process-list abs">
  <li>Ledgerwise Reach offer expert demand generation support, from providing detailed leads of qualified decision-makers, to a comprehensive lead generation and SQL service.</li>
  <li>Our extensive and ongoing research campaigns give you the ability to build contact lists that identify individuals at all stages of the buying cycle, from pre-sales to sales ready.</li>
  <li>With access to over 31 million names, Ledgerwise Reach offers a range of marketing options that allow you to use our data to target the decision makers you need to reach.<br><strong>This can include:</strong>
    <span class="sub">• Breakdown by geography, job title, role and responsibility</span>
    <span class="sub">• Targeting through previous research and buying intention</span>
    <span class="sub">• Email dispatch to selected individuals</span>
    Extensive telemarketing options</li>
</ul>

<p class="estimate abs">Estimate our Fees Using the<br>Calculator Below!</p>

<section class="calculator abs"></section>
<h3 class="calc-title abs">DEMAND GROWTH PRICING CALCULATOR</h3>
<label class="calc-label abs">Enter average Media Spendings here:</label>
<input class="calc-input abs" type="text" aria-label="Average media spendings">
<div class="calc-button abs">CALCULATE</div>

<section class="services-bg abs"></section>
<div class="services-box abs"></div>
<div class="services-feature abs"></div>
<h2 class="services-title abs">OUR<br>SERVICES</h2>
<svg class="feature-icon abs" width="160" height="72" viewBox="0 0 160 72" aria-hidden="true">
  <g fill="#8d93a6"><circle cx="28" cy="14" r="11"/><circle cx="62" cy="14" r="11"/><circle cx="96" cy="14" r="11"/><circle cx="130" cy="14" r="11"/>
  <path d="M10 50a18 18 0 0 1 36 0v6H10z"/><path d="M44 50a18 18 0 0 1 36 0v6H44z"/><path d="M78 50a18 18 0 0 1 36 0v6H78z"/><path d="M112 50a18 18 0 0 1 36 0v6h-36z"/>
  <circle cx="45" cy="34" r="11"/><circle cx="113" cy="34" r="11"/><path d="M25 72a20 20 0 0 1 40 0z"/><path d="M93 72a20 20 0 0 1 40 0z"/></g>
</svg>
<h3 class="feature-title abs">MARKETING QUALIFIED LEADS (MQL)</h3>
<p class="feature-copy abs">A Marketing Qualified Lead (MQL) is a prospect that has expressed an interest in what your brand has to offer. An MQL has taken the first steps to becoming a customer and is ready to receive additional contact from your company. From a very general perspective: Marketing Qualified Leads turn into Sales Qualified Leads (SQLs), which in turn can convert into customers once they have been through the buyer's journey. It's important for each potential customer to travel through all stages of the buying journey and the MQL is the first step in this process. This engagement warms them up to your brand, builds trust and puts them in the position to consider your solution as the right fit for their business.</p>
<div class="dots feature-dots abs"><span class="on"></span><span></span><span></span></div>

<div class="service-col abs" style="left:40px">
  <svg width="120" height="50" viewBox="0 0 160 72" aria-hidden="true"><g fill="#8d93a6"><circle cx="28" cy="14" r="11"/><circle cx="62" cy="14" r="11"/><circle cx="96" cy="14" r="11"/><circle cx="130" cy="14" r="11"/><path d="M10 50a18 18 0 0 1 36 0v6H10z"/><path d="M112 50a18 18 0 0 1 36 0v6h-36z"/><circle cx="45" cy="34" r="11"/><circle cx="113" cy="34" r="11"/><path d="M25 72a20 20 0 0 1 40 0z"/><path d="M93 72a20 20 0 0 1 40 0z"/></g></svg>
  <h4>MARKETING QUALIFIED LEADS (MQL)</h4>
  <p>The MQL is the foundation of a B2B demand generation strategy and helps businesses identify those prospects who could be in the market for their solutions.</p>
</div>
<div class="service-divider abs" style="left:398px"></div>
<div class="service-col abs" style="left:420px">
  <svg width="84" height="58" viewBox="0 0 84 58" aria-hidden="true"><g fill="#8d93a6"><circle cx="20" cy="12" r="9"/><circle cx="64" cy="12" r="9"/><path d="M4 42a16 16 0 0 1 32 0v4H4z"/><path d="M48 42a16 16 0 0 1 32 0v4H48z"/><circle cx="42" cy="24" r="11"/><path d="M20 58a22 22 0 0 1 44 0z"/></g></svg>
  <h4>ACCOUNT BASED MARKETING LEADS (ABM)</h4>
  <p>ABM is a strategy that directs marketing resources to engaging a specific set of target accounts.</p>
</div>
<div class="service-divider abs" style="left:800px"></div>
<div class="service-col abs" style="left:777px">
  <svg width="50" height="62" viewBox="0 0 50 62" aria-hidden="true"><g fill="#8d93a6"><circle cx="25" cy="14" r="13"/><path d="M2 62V50a23 23 0 0 1 46 0v12z"/></g></svg>
  <h4>SALES QUALIFIED LEAD / BANT</h4>
  <p>An SQL lead or a BANT lead is a type of lead that expressed a specific interest in a product and service that you have to offer...</p>
</div>

<div class="voices abs"></div>
<p class="voices-text abs">See What our customers say about us!</p>
<h2 class="testimonials-title abs">TESTIMONIALS</h2>
<svg class="abs" style="left:790px;top:4240px" width="70" height="60" viewBox="0 0 70 60" aria-hidden="true"><path d="M0 0H70L8 60Z" fill="#fff"/></svg>
<div class="quote-card abs"></div>
<div class="quote-mark abs" aria-hidden="true">“</div>
<p class="quote-label abs">QUOTE</p>
<p class="quote-copy abs">Lorem ipsum dolor sit amet, consectetur adipiscing elit, sed do eiusmod tempor incididunt ut labore et dolore magna aliqua. Quis ipsum suspendisse ultrices gravida. Risus commodo viverra maecenas accumsan lacus vel facilisis.</p>
<p class="quote-name abs">Jane Doe</p>
<div class="quote-close abs" aria-hidden="true">”</div>
<div class="dots quote-dots abs"><span class="on"></span><span></span><span></span></div>

<div class="apart-side abs"></div>
<h2 class="apart-title abs">WHAT SETS US APART?</h2>
<section class="apart-box abs"></section>
<h3 class="apart-sub abs">Our Proprietary QA Technology</h3>
<div class="apart-copy abs">
  <p><span class="wordmark">PROSPORA</span>is a proprietary lead verification platform from Ledgerwise Reach that aims to sift out invalid leads with questionable or erroneous data. The platform is designed to equip sales teams with accurate, high-quality records in order to improve lead generation, accelerate pipeline and increase revenue.</p>
  <p>Prospora is positioned to quickly identify, validate, and improve lead quality at the point-of-entry by filtering out all leads that do not match required filters, such as job title, company size, etc. The platform is designed to use real-time contact validation and live phone verification to remove all duplicate leads, as well as leads with invalid data components. Users can also build their own rules-based, post-submission verification protocol on our forms.</p>
</div>

<footer class="site-footer abs"></footer>
<div class="footer-brand abs">
  <span class="brand-dot" style="display:block"></span>
  <div class="brand-name">ledgerwise reach</div>
  <div class="brand-tag">The Demand Generation Company</div>
</div>
<div class="footer-rule abs" style="left:272px"></div>
<ul class="footer-links abs">
  <li class="footer-head" style="margin-top:0">Go To</li>
  <li>Prospora &amp; QA Technology</li><li>Services</li><li>About Us</li><li>Intent Data</li><li>Testimonials</li>
</ul>
<div class="footer-rule abs" style="left:536px"></div>
<div class="footer-tech abs">
  <div class="footer-head">Technologies</div>
  <div class="item">MQL</div><div class="item">SQL</div><div class="item">ABM</div>
  <div style="width:80px;height:1px;background:#525a72;margin:38px auto 0"></div>
</div>
<div class="footer-location abs">
  <div class="footer-head" style="margin-left:30px">Location</div>
  <div style="margin-top:14px;display:flex;align-items:center;gap:8px">
    <svg width="14" height="20" viewBox="0 0 14 20" aria-hidden="true"><path d="M7 0a7 7 0 0 1 7 7c0 5-7 13-7 13S0 12 0 7a7 7 0 0 1 7-7z" fill="#fff"/><circle cx="7" cy="7" r="2.6" fill="#0c1228"/></svg>
    London, UK
  </div>
</div>
<div class="footer-rule abs" style="left:720px"></div>
<div class="footer-about abs">
  <div class="footer-head">About Us</div>
  <p>Ledgerwise Reach can deliver high quality sales leads from any country in the world. This can include leads via email or telemarketing, account-based targeting (ABM) or identifying need and pain points through BANT / SQL campaigns.</p>
</div>
<div class="btn-outline footer-contact abs">Contact Us</div>

</body>
</html>
```